Sudden Tides "Lantern Road" New Single Cover

Create cover artwork for the band Sudden Tides' new single "Lantern Road" being released early 2020. Style, font and graphics to be consistent with band's previous releases and overall brand identity. Visit www.suddentidesband.example and our Spotify page https://music.example.net/artist/7QzWpLx3RtVnKd8e2YbHcJ?si=MUrTgKa4PLe7skvWq2AmZd to view our previous releases and overall brand identity. Some examples attached as well. We are looking for someone to work with on future projects as well.

Lyrics are here: https://docs.example.org/document/d/3KTp9wrn_2ZQa8eXb4Lo_fimH7C5m83Jz4Pd70hrtVcA/edit

Music is here: https://audiostream.example.com/suddentides/lantern-road/s-pzkwa

Font styles to use
Sans Serif

Colors

Designer to choose colors to be used in the design.

Requirements
Must have
• Must be consistent with current brand identity and with prior album / single art.

```html
<!DOCTYPE html>
<html lang="en">
<head>
<meta charset="utf-8">
<title>Sudden Tides – Lantern Road</title>
<link rel="stylesheet" href="https://fonts.googleapis.com/css2?family=Jost:wght@400;500&display=swap">
<style>
  :root {
    --teal: #16a6ac;
    --tile: #2ea7ad;
    --glow: #5de6a9;
    --yellow: #fdb019;
    --orange: #f68920;
    --mauve: #af7b8a;
    --violet: #6b6ca8;
    --navy: #1c2b58;
    --white: #ffffff;
  }
  html, body {
    margin: 0;
    padding: 0;
    overflow: hidden;
    background: var(--teal);
  }
  .cover {
    position: relative;
    width: 1200px;
    height: 1200px;
    background: var(--teal);
    overflow: hidden;
    font-family: "Jost", "Futura", sans-serif;
  }
  .cover__title {
    position: absolute;
    inset: 0;
    width: 1200px;
    height: 1200px;
  }
  .cover__title text {
    font-family: "Jost", "Futura", sans-serif;
    font-weight: 400;
  }
  .c-yellow { fill: var(--yellow); }
  .c-orange { fill: var(--orange); }
  .c-mauve  { fill: var(--mauve); }
  .c-violet { fill: var(--violet); }
  .c-navy   { fill: var(--navy); }

  .artist-band {
    position: absolute;
    left: 0;
    top: 1035px;
    width: 1200px;
    height: 97px;
    border-top: 1px solid var(--white);
    border-bottom: 1px solid var(--white);
    box-sizing: border-box;
    display: flex;
    align-items: center;
    justify-content: center;
  }
  .artist-band__name {
    margin: 0;
    color: var(--white);
    font-family: "Jost", "Futura", sans-serif;
    font-weight: 500;
    font-size: 78px;
    line-height: 1;
    letter-spacing: 0.12em;
    padding-left: 0.12em;
    text-transform: uppercase;
  }
</style>
</head>
<body>
  <main class="cover">
    <svg class="cover__title" viewBox="0 0 1200 1200" xmlns="http://www.w3.org/2000/svg" aria-label="Lantern Road">
      <defs>
        <radialGradient id="burst-glow" cx="50%" cy="50%" r="55%">
          <stop offset="0%" stop-color="#2ea7ad"/>
          <stop offset="45%" stop-color="#5de6a9" stop-opacity="0.55"/>
          <stop offset="100%" stop-color="#2ea7ad"/>
        </radialGradient>
      </defs>

      <text class="title-line title-line--top" x="600" y="498" font-size="272" text-anchor="middle"><tspan class="c-yellow">L</tspan><tspan class="c-orange">A</tspan><tspan class="c-mauve">N</tspan><tspan class="c-violet">T</tspan><tspan class="c-navy">E</tspan><tspan class="c-yellow">R</tspan><tspan class="c-orange">N</tspan></text>

      <text class="title-line title-line--bottom" x="60" y="862" font-size="380"><tspan class="c-violet">R</tspan></text>

      <g class="title-sunburst" role="img" aria-label="Radiating sunburst of thin mint lines standing in for the letter O">
        <rect x="322" y="555" width="306" height="325" fill="var(--tile)"/>
        <rect x="322" y="555" width="306" height="325" fill="url(#burst-glow)"/>
      </g>

      <text class="title-line title-line--bottom" x="648" y="862" font-size="380"><tspan class="c-yellow">A</tspan><tspan class="c-orange">D</tspan></text>
    </svg>

    <div class="artist-band">
      <h1 class="artist-band__name">Sudden Tides</h1>
    </div>
  </main>
</body>
</html>
```